3" Round Business Card for Funeral Home

We need a business card designed for our cremation service. We would like to use a 3" round business card.

The business card will be 2-sided. One side with the logo featured prominently. The back sad will have employee name and contact info.

Templates for printing have been attached to project as well as logo

We like soft colors like the logo. Final design should promote a feeling of trust.

Industry/Entity Type

Funeral

Contact Information for Business Card

Employee Name, Phone number, email, web address

Requirements
Should not have
• any sort of funeral item such as urn, casket, hearse, tombstone

```html
<!DOCTYPE html>
<html lang="en">
<head>
<meta charset="utf-8">
<title>Round Business Card – Restful Path</title>
<link rel="stylesheet" href="https://fonts.googleapis.com/css2?family=Poppins:wght@400&family=Yellowtail&display=swap">
<style>
  :root {
    --backdrop: #9a9a9a;
    --card-white: #ffffff;
    --brand-purple: #92278f;
    --brand-teal: #16a79c;
    --text-grey: #555555;
    --rule-grey: #8a8a8a;
  }
  html, body {
    margin: 0;
    padding: 0;
    width: 1125px;
    height: 1200px;
    overflow: hidden;
    background: var(--backdrop);
  }
  .stage {
    position: relative;
    width: 1125px;
    height: 1200px;
  }
  .card {
    position: absolute;
    top: 347px;
    width: 466px;
    height: 466px;
    border-radius: 50%;
    box-shadow: 2px 4px 10px rgba(0,0,0,0.35);
  }
  .card-front {
    left: 64px;
    background: var(--card-white);
  }
  .card-back {
    left: 585px;
    background: var(--brand-purple);
    display: flex;
    align-items: center;
    justify-content: center;
  }
  .person-name {
    position: absolute;
    left: 86px;
    top: 88px;
    margin: 0;
    font-family: "Yellowtail", cursive;
    font-weight: 400;
    font-size: 52px;
    line-height: 1;
    white-space: nowrap;
  }
  .first-name { color: var(--brand-teal); }
  .last-name { color: var(--brand-purple); }
  .name-rule {
    position: absolute;
    left: 83px;
    top: 160px;
    width: 302px;
    height: 1px;
    background: var(--rule-grey);
  }
  .job-title {
    position: absolute;
    left: 85px;
    top: 166px;
    margin: 0;
    font-family: "Poppins", sans-serif;
    font-size: 17px;
    color: var(--brand-purple);
  }
  .address {
    position: absolute;
    left: 86px;
    top: 230px;
    margin: 0;
    font-family: "Poppins", sans-serif;
    font-style: normal;
    font-size: 18px;
    line-height: 23px;
    color: var(--text-grey);
  }
  .contact-list {
    position: absolute;
    left: 86px;
    top: 293px;
    margin: 0;
    padding: 0;
    list-style: none;
    font-family: "Poppins", sans-serif;
    font-size: 18px;
    line-height: 23.5px;
    color: var(--text-grey);
  }
  .contact-item {
    display: flex;
    align-items: center;
    gap: 11px;
  }
  .contact-icon {
    width: 16px;
    height: 16px;
    fill: var(--brand-teal);
    flex: none;
  }
  .brand-name {
    margin: 0;
    font-family: "Poppins", sans-serif;
    font-weight: 400;
    font-size: 50px;
    color: var(--card-white);
    letter-spacing: -0.5px;
  }
</style>
</head>
<body>
<main class="stage">
  <section class="card card-front">
    <h1 class="person-name"><span class="first-name">Daniel</span> <span class="last-name">Brooks</span></h1>
    <div class="name-rule"></div>
    <p class="job-title">Founder &amp; CEO</p>
    <address class="address">412 Willow Bend Road<br>Fairbanks, Alaska 99701</address>
    <ul class="contact-list">
      <li class="contact-item">
        <svg class="contact-icon" viewBox="0 0 16 16" aria-hidden="true"><path d="M3.6 1.2l2.3 2.6-1.3 1.8c.9 2 2.4 3.5 4.4 4.5l1.8-1.3 2.6 2.3-1.3 2.3C7 13.3 2.6 9 1.3 2.5z"/></svg>
        <span>555-014-2287</span>
      </li>
      <li class="contact-item">
        <svg class="contact-icon" viewBox="0 0 16 16" aria-hidden="true"><path d="M1 4h14v9H1z M2.2 5l5.8 4.3L13.8 5" fill="none" stroke="#16a79c" stroke-width="1.6"/></svg>
        <span>hello@restfulpath.com</span>
      </li>
      <li class="contact-item">
        <svg class="contact-icon" viewBox="0 0 16 16" aria-hidden="true"><circle cx="8" cy="8" r="7"/><path d="M5 4.5c1.5 0 2 1.3 1.3 2.4-.8 1.1.4 2 1.5 2.2 1 .2.7 2-.3 2.8M10.5 3.5c-.7 1 .2 1.8 1.2 1.7" fill="none" stroke="#fff" stroke-width="1.2"/></svg>
        <span>www.restfulpath.com</span>
      </li>
    </ul>
  </section>
  <section class="card card-back">
    <p class="brand-name">restfulpath.com</p>
  </section>
</main>
</body>
</html>
```